I need a business card designed using the logo provided either vertical or horizontal......Tallowmere Advisory is an Australian based real estate company that caters for the upper end of the market so the design of the business card "must reflect" the companies image!!
Colour combinations are optional but "must be realistic" and must be able to be accurately useable CMYK colours.
Please consider that any colours used "must be able to be used" and be suitable in following designs for "pull out banner signs" and "real estate signs".
The colours and the font in the attached designs are for example and other combinations are encouraged.
Target Market(s)
The High End of the Australian real estate market
Industry/Entity Type
Business
Contact Information for Business Card
Logo - Business Name - Director + Licensed Real Estate Agent - Mobile Number (Cell Phone) - Business Number - Fax - Email Address - Web address
Requirements
Must have
- Designs and colours (CMYK) that can easily be interpreted by an Australian printer.
Nice to have
- Some alternative ideas on colour and font..........the ones provided are ok and have been provided as an example but I am looking for alternative ideas
Should not have
- Loud, overly bright colours. Designs that do not reflect the professional standards of the business.
- Designs that look good on a computer monitor but can not be re-created on a printing press.............this is most important when it comes to shading etc.

```html
<!DOCTYPE html>
<html lang="en">
<head>
<meta charset="utf-8">
<title>Tallowmere Advisory – Business Card</title>
<link href="https://fonts.googleapis.com/css2?family=Michroma&family=Open+Sans:wght@400;600;700&display=swap" rel="stylesheet">
<style>
  :root {
    --backdrop: #e4e4e4;
    --card-black: #0c0c0c;
    --card-charcoal: #262626;
    --gold: #c9923c;
    --gold-light: #e6c27a;
    --gold-pale: #e8d29c;
    --gold-deep: #a8702a;
    --white: #ffffff;
    --ink: #1e1608;
  }
  * { margin: 0; padding: 0; box-sizing: border-box; }
  html, body { width: 1200px; height: 852px; overflow: hidden; }
  body {
    background: var(--backdrop);
    font-family: "Open Sans", sans-serif;
    position: relative;
  }
  .card {
    position: absolute;
    top: 276px;
    width: 520px;
    height: 300px;
    border-radius: 22px;
    overflow: hidden;
    background: radial-gradient(ellipse at 45% 35%, var(--card-charcoal) 0%, var(--card-black) 70%);
    box-shadow: 0 8px 22px rgba(0,0,0,0.25);
  }
  .card--front { left: 50px; }
  .card--back { left: 630px; }

  .brand {
    display: flex;
    align-items: center;
    gap: 14px;
  }
  .brand__mark {
    width: 18px; height: 18px;
    background: var(--gold);
    flex-shrink: 0;
  }
  .brand__name {
    font-family: "Michroma", sans-serif;
    color: var(--white);
    text-transform: uppercase;
    letter-spacing: 1px;
    white-space: nowrap;
  }
  .card--front .brand {
    position: absolute;
    left: 50%; top: 50%;
    transform: translate(-50%, -50%);
  }
  .card--front .brand__name { font-size: 21px; }

  .card--back .brand {
    position: absolute;
    left: 30px; top: 42px;
  }
  .card--back .brand__mark { width: 14px; height: 14px; }
  .card--back .brand__name { font-size: 15px; }

  .holder {
    position: absolute;
    right: 30px; top: 58px;
    text-align: right;
  }
  .holder__name {
    color: var(--gold-pale);
    font-weight: 700;
    font-size: 15px;
  }
  .holder__role {
    color: var(--white);
    font-size: 11px;
    margin-top: 2px;
  }

  .divider {
    position: absolute;
    left: 30px; right: 30px; top: 108px;
    height: 1.5px;
    background: linear-gradient(90deg, var(--gold-deep), var(--gold-light), var(--gold));
  }

  .contacts {
    position: absolute;
    left: 30px; top: 130px;
    list-style: none;
    color: var(--white);
    font-size: 12.5px;
    font-weight: 600;
  }
  .contacts li {
    display: flex;
    align-items: center;
    gap: 10px;
    height: 24px;
  }
  .contacts svg { width: 13px; height: 13px; flex-shrink: 0; }
  .contacts .pair { display: flex; align-items: center; gap: 10px; }
  .contacts .pair + .pair { margin-left: 8px; }

  .address-band {
    position: absolute;
    left: 0; right: 0; bottom: 0;
    height: 54px;
    background: linear-gradient(90deg, var(--gold-deep) 0%, var(--gold) 25%, var(--gold-light) 55%, var(--gold) 80%, var(--gold-deep) 100%);
    display: flex;
    align-items: center;
    padding-left: 30px;
    color: var(--ink);
    font-size: 12.5px;
    font-weight: 600;
  }
</style>
</head>
<body>

  <section class="card card--front" aria-label="Card front">
    <div class="brand">
      <span class="brand__mark"></span>
      <span class="brand__name">Tallowmere Advisory</span>
    </div>
  </section>

  <section class="card card--back" aria-label="Card back">
    <div class="brand">
      <span class="brand__mark"></span>
      <span class="brand__name">Tallowmere Advisory</span>
    </div>

    <div class="holder">
      <p class="holder__name">Your Long Name</p>
      <p class="holder__role">Managing Director</p>
    </div>

    <div class="divider"></div>

    <ul class="contacts">
      <li>
        <span class="pair">
          <svg viewBox="0 0 16 16" aria-hidden="true"><path fill="#c9923c" d="M3 1.5l3 .5 1 3.2-1.8 1.3a9 9 0 004.3 4.3l1.3-1.8 3.2 1 .5 3-2 1.5C6.5 14 2 9.5 1.5 3.5z"/></svg>
          00.00.00.0000
        </span>
        <span class="pair">
          <svg viewBox="0 0 16 16" aria-hidden="true"><rect x="4" y="1" width="8" height="5" fill="#c9923c"/><rect x="1" y="6" width="14" height="6" rx="1" fill="#c9923c"/><rect x="4" y="10" width="8" height="5" fill="#e6c27a"/></svg>
          00.00.00.0000
        </span>
      </li>
      <li>
        <svg viewBox="0 0 16 16" aria-hidden="true"><rect x="1" y="3" width="14" height="10" rx="1" fill="#c9923c"/><path d="M1.5 3.5L8 9l6.5-5.5" stroke="#0c0c0c" stroke-width="1.3" fill="none"/></svg>
        yourname@yourwebsite.com
      </li>
      <li>
        <svg viewBox="0 0 16 16" aria-hidden="true"><g stroke="#c9923c" stroke-width="1.3" fill="none"><circle cx="8" cy="8" r="6.5"/><ellipse cx="8" cy="8" rx="3" ry="6.5"/><path d="M1.5 8h13"/></g></svg>
        www.yourwebsite.com
      </li>
    </ul>

    <div class="address-band">Your Commercial or office address with pin code</div>
  </section>

</body>
</html>
```